Modern HomePage Design for Church

We are looking for a modern homepage design using the sections we put together in the template. The colors we want are blue, black, grey, and white. We do not want use the colors in the logo. Please modify the logo color to match the website color scheme.

Target Market(s)

Church

Industry/Entity Type

Church

Number of Pages Required

1 page

Colors
0293ce
ffffff
474747
9d9d9d

```html
<!DOCTYPE html>
<html lang="en">
<head>
<meta charset="utf-8">
<title>Gracefield Church – Home</title>
<link href="https://fonts.googleapis.com/css2?family=Poppins:wght@400;500;600;700&family=Open+Sans:wght@400;600&display=swap" rel="stylesheet">
<style>
:root{
  --primary:#0293ce;
  --primary-soft:#e3f4fb;
  --primary-line:#a9dcf1;
  --dark:#1b1d21;
  --dark-2:#2a2d33;
  --ink:#111418;
  --text:#474747;
  --muted:#9d9d9d;
  --line:#e6e6e6;
  --white:#ffffff;
}
*{box-sizing:border-box;margin:0;padding:0}
html,body{width:1200px;height:4317px;overflow:hidden}
body{position:relative;background:var(--white);font-family:"Open Sans",sans-serif;color:var(--text);font-size:14px;line-height:1.75}
h1,h2,h3,h4{font-family:"Poppins",sans-serif;color:var(--ink)}
.abs{position:absolute}
.btn{display:inline-block;font-family:"Poppins",sans-serif;font-weight:600;font-size:12px;letter-spacing:1.5px;text-transform:uppercase;padding:0 30px;line-height:44px;color:var(--white);background:var(--primary)}
.btn-soft{background:var(--primary-soft);color:var(--primary);line-height:40px;font-size:11px;padding:0 26px}
.center{text-align:center}
.pic{position:absolute}

/* hero */
.hero{left:0;top:0;width:1200px;height:705px;background:linear-gradient(135deg,#2b3036 0%,#16191d 55%,#23323d 100%)}
.hero-title{left:0;top:236px;width:1200px;text-align:center;color:var(--white);font-size:48px;font-weight:700;letter-spacing:.5px}
.hero-sub{left:380px;top:316px;width:440px;text-align:center;color:#d6d9dd;font-size:14px;line-height:1.6}
.hero-btn{left:511px;top:394px}
.arrow{position:absolute;width:14px;height:14px;border-left:2px solid rgba(255,255,255,.6);border-bottom:2px solid rgba(255,255,255,.6)}

/* info cards */
.card{background:var(--white);box-shadow:0 8px 30px rgba(0,0,0,.1)}
.card .label{font-family:"Poppins",sans-serif;font-size:10px;font-weight:600;letter-spacing:1px;color:var(--ink);text-transform:uppercase}
.card .title{font-family:"Poppins",sans-serif;font-size:21px;font-weight:600;color:var(--ink);margin-top:4px}
.date{font-family:"Poppins",sans-serif;color:var(--primary);font-weight:600;text-align:center}
.date b{display:block;font-size:36px;line-height:1}
.date span{font-size:10px;letter-spacing:1px;color:var(--ink)}
.meta{font-size:12px;color:var(--text);line-height:1.8}
.meta svg{vertical-align:-2px;margin-right:8px}
.iconbox{display:inline-block;width:40px;height:40px;border:1px solid var(--line);margin-right:8px;position:relative}
.iconbox svg{position:absolute;left:12px;top:12px}

/* about */
.about-title{left:0;top:1048px;width:1200px;text-align:center;font-size:30px;font-weight:600;line-height:1.35}
.about-title u{text-decoration-color:var(--primary)}
.about-text{left:310px;top:1168px;width:580px;text-align:center;font-size:13px}
.about-text p+p{margin-top:16px}

/* dark band */
.band{left:0;top:1568px;width:1200px;height:527px;background:linear-gradient(160deg,#2b3036,#17191d 60%,#25313a)}
.nav{left:0;top:1568px;width:1200px;height:50px;background:var(--dark)}
.logo{font-family:"Poppins",sans-serif;font-weight:700;color:var(--white);font-size:24px;line-height:1}
.logo small{display:block;font-size:9px;letter-spacing:2px;font-weight:400;color:var(--muted);margin-top:3px;margin-left:22px}
.logo-mark{display:inline-block;width:14px;height:14px;background:var(--primary);margin-right:8px}
.menu{left:430px;top:1585px;display:flex;gap:24px;font-family:"Poppins",sans-serif;font-size:11px;font-weight:500;color:var(--white);letter-spacing:.5px}
.menu span::after{content:"";display:inline-block;width:4px;height:4px;border-right:1px solid #fff;border-bottom:1px solid #fff;transform:rotate(45deg);margin-left:6px;vertical-align:3px}
.donate-btn{left:935px;top:1576px;width:106px;height:36px;line-height:36px;text-align:center;background:var(--primary);color:var(--white);font-family:"Poppins",sans-serif;font-weight:600;font-size:11px;letter-spacing:1px}
.eyebrow{font-family:"Poppins",sans-serif;font-weight:600;font-size:11px;letter-spacing:1.5px;color:var(--primary);text-transform:uppercase}
.slide-title{left:0;top:1690px;width:1200px;text-align:center;color:var(--white);font-size:28px;font-weight:600}
.slide-text{left:380px;top:1740px;width:440px;text-align:center;color:#d6d9dd;font-size:13px;line-height:1.7}
.raised{font-family:"Poppins",sans-serif;font-size:12px;color:#d6d9dd}
.raised b{color:var(--white)}

/* events & sermons */
.sec-head{display:flex;justify-content:space-between;align-items:center;border-bottom:1px solid var(--line);padding-bottom:16px}
.sec-head h3{font-size:22px;font-weight:600}
.see-all{font-family:"Poppins",sans-serif;font-size:9px;letter-spacing:1px;color:var(--primary);background:var(--primary-soft);padding:0 18px;line-height:26px}
.event{position:absolute;left:164px;width:426px;height:115px;border:1px solid var(--line);background:var(--white)}
.event .date{position:absolute;left:24px;top:28px;width:50px}
.event .date b{font-size:32px}
.event .body{position:absolute;left:106px;top:22px}
.event h4{font-size:15px;font-weight:600;margin-bottom:6px}
.acc{position:absolute;left:685px;width:355px;border-bottom:1px solid var(--line);font-family:"Poppins",sans-serif;font-size:14px;font-weight:600;color:var(--ink);padding-bottom:16px}
.acc::after{content:"+";position:absolute;right:4px;top:-4px;font-weight:300;color:var(--muted);font-size:20px}
.acc.open::after{content:"–"}

/* history */
.history h3{font-size:20px;font-weight:600;margin-bottom:14px}
.history p{font-size:13px}
.more{display:block;color:var(--primary);font-size:12px;margin-top:14px;text-decoration:underline}
.quote-box{left:538px;top:2872px;width:662px;height:294px;background:var(--dark)}
.quote-text{left:580px;top:2982px;width:480px;color:var(--white);font-size:15px;line-height:1.75}
.quote-mark{left:580px;top:2938px;color:var(--primary);font-family:"Poppins",sans-serif;font-size:40px;font-weight:700;line-height:1}
.quote-author{left:580px;top:3110px;color:var(--white);font-family:"Poppins",sans-serif;font-size:11px;font-weight:600;letter-spacing:1px}

/* news */
.news-title{left:0;top:3262px;width:1200px;text-align:center;font-size:30px;font-weight:600}
.news-card{position:absolute;top:3353px;width:426px;height:504px}
.news-card .body{position:absolute;left:24px;top:202px;width:378px;height:300px;background:var(--white);box-shadow:0 10px 30px rgba(0,0,0,.09);text-align:center;padding:28px 30px}
.news-card .d{font-size:11px;color:var(--primary)}
.news-card h4{font-size:19px;font-weight:600;margin:4px 0 14px}
.news-card p{font-size:13px;margin-bottom:26px}

/* footer */
.subscribe{left:0;top:3885px;width:1200px;height:78px;background:var(--dark)}
.footer h4{font-size:17px;font-weight:600;margin-bottom:18px}
.footer p,.footer li{font-size:12px;line-height:2}
.footer ul{list-style:none}
.bottom{left:160px;top:4252px;width:880px;display:flex;justify-content:space-between;font-size:12px;color:var(--text)}
.bottom nav{display:flex;gap:30px}
</style>
</head>
<body>

<!-- Hero -->
<section class="abs hero" role="img" aria-label="Priest in vestments praying with hands clasped at the altar, tinted dark"></section>
<h1 class="abs hero-title">GOD GIVES US POWER</h1>
<p class="abs hero-sub">There are many variations of passages of Lorem Ipsum available, but the majority have suffered alteration in some</p>
<span class="abs btn hero-btn">Explore Events</span>
<span class="arrow" style="left:52px;top:358px;transform:rotate(45deg)"></span>
<span class="arrow" style="left:1134px;top:358px;transform:rotate(-135deg)"></span>

<!-- Next event card -->
<article class="abs card" style="left:164px;top:668px;width:426px;height:282px;padding:30px 24px">
  <div class="label">Next Event</div>
  <div class="title">Which is the same as saying</div>
  <div style="border-top:1px solid var(--line);margin-top:14px;padding-top:20px;display:flex;gap:26px">
    <div class="date" style="width:50px"><b>20</b><span>AUG'18</span></div>
    <div class="meta">
      <div><svg width="10" height="10" viewBox="0 0 10 10"><circle cx="5" cy="5" r="4" fill="none" stroke="#0293ce" stroke-width="1.4"/><path d="M5 2.5V5h2" stroke="#0293ce" fill="none"/></svg>Sunday (8:00 - 9:00 am)</div>
      <div style="display:flex"><svg width="10" height="12" viewBox="0 0 10 12" style="margin-top:6px;flex:none"><path d="M5 11C2 7 1 5.5 1 4a4 4 0 018 0c0 1.5-1 3-4 7z" fill="#0293ce"/></svg><span>18 Willow Bend Lane, Maple Falls,<br>OR, United States</span></div>
    </div>
  </div>
  <span class="btn btn-soft" style="position:absolute;left:24px;top:206px">Join Now ›</span>
</article>

<!-- Latest sermon card -->
<article class="abs card" style="left:613px;top:668px;width:426px;height:282px;padding:30px 24px">
  <div class="label">Latest Sermons</div>
  <div class="title">We denounce with righteous</div>
  <div class="meta" style="margin-top:10px"><svg width="10" height="10" viewBox="0 0 10 10"><circle cx="5" cy="3" r="2.4" fill="#0293ce"/><path d="M0.5 10a4.5 4.5 0 019 0z" fill="#0293ce"/></svg>Message from <u>Nathaniel</u> &nbsp;&nbsp;&nbsp;<svg width="10" height="10" viewBox="0 0 10 10"><rect x="1" y="2" width="8" height="7" fill="none" stroke="#0293ce"/><path d="M1 4h8" stroke="#0293ce"/></svg>Aug 12, 2018</div>
  <div style="margin-top:14px">
    <span class="iconbox"><svg width="16" height="16" viewBox="0 0 16 16"><rect x="1" y="4" width="14" height="9" rx="2" fill="#9d9d9d"/><path d="M7 6.5v4l3.5-2z" fill="#fff"/></svg></span>
    <span class="iconbox"><svg width="16" height="16" viewBox="0 0 16 16"><path d="M4 1h6l3 3v11H4z" fill="none" stroke="#9d9d9d" stroke-width="1.4"/></svg></span>
    <span class="iconbox"></span>
  </div>
  <div style="position:absolute;left:24px;top:210px;width:300px;height:40px;background:var(--primary-soft)">
    <svg width="10" height="12" viewBox="0 0 10 12" style="position:absolute;left:14px;top:14px"><path d="M0 0l10 6-10 6z" fill="#0293ce"/></svg>
    <span style="position:absolute;left:38px;top:10px;font-size:10px;color:var(--primary)">0:00</span>
    <span style="position:absolute;left:70px;top:19px;width:180px;height:2px;background:var(--primary-line)"></span>
  </div>
  <div style="position:absolute;left:334px;top:210px;width:40px;height:40px;background:var(--primary-soft);text-align:center;line-height:40px;color:var(--primary);font-size:12px">»</div>
</article>

<!-- About -->
<div class="pic" style="left:0;top:1135px;width:330px;height:220px;background:linear-gradient(90deg,#dcdfe2,#eef0f2 80%,rgba(255,255,255,0))" role="img" aria-label="Sketch illustration of an adobe mission chapel with a cactus"></div>
<div class="pic" style="left:1105px;top:1148px;width:95px;height:190px;background:linear-gradient(270deg,#dcdfe2,rgba(255,255,255,0))" role="img" aria-label="Sketch illustration of a traveller riding a donkey"></div>
<h2 class="abs about-title">We are a Church That<br>Believes in <u>Jesus</u></h2>
<div class="abs about-text">
  <p>Many desktop publishing packages and web page editors now use Lorem Ipsum as their default model text, and a search for 'lorem ipsum' will uncover many web sites still in their infancy. Various versions have evolved over the years, sometimes by accident, sometimes on purpose (injected humour and the like). If you are going to use a passage of Lorem Ipsum.</p>
  <p>You need to be sure there isn't anything embarrassing hidden in the middle of text. All the Lorem Ipsum generators on the Internet tend to repeat predefined chunks as necessary.</p>
</div>
<span class="abs btn" style="left:511px;top:1402px">Explore Events</span>

<!-- Dark band with navigation and cause slider -->
<section class="abs band" role="img" aria-label="Church interior with wooden pews, tinted dark"></section>
<header class="abs nav"></header>
<div class="abs logo" style="left:160px;top:1578px"><span class="logo-mark"></span>Gracefield<small>CHURCH THEME</small></div>
<nav class="abs menu"><span>HOME</span><span>TEMPLATES</span><span>ELEMENTS</span><span>LANDING</span><span>PAGES</span></nav>
<svg class="abs" style="left:868px;top:1586px" width="16" height="14" viewBox="0 0 16 14"><path d="M8 13L1.5 6.5a3.6 3.6 0 015.2-5L8 3l1.3-1.5a3.6 3.6 0 015.2 5z" fill="#fff"/></svg>
<svg class="abs" style="left:903px;top:1586px" width="16" height="14" viewBox="0 0 16 14"><path d="M1 1h2.5l2 8h8l1.5-6H5" fill="none" stroke="#fff" stroke-width="1.5"/><circle cx="6.5" cy="12" r="1.3" fill="#fff"/><circle cx="12.5" cy="12" r="1.3" fill="#fff"/></svg>
<div class="abs donate-btn">DONATE</div>

<div class="abs eyebrow center" style="left:0;top:1645px;width:1200px">Urgent Causes</div>
<h2 class="abs slide-title">The Five Points of Gospel Truth</h2>
<p class="abs slide-text">Many desktop publishing packages and web page editors now use Lorem Ipsum as their default model text, and a search for</p>
<div class="abs raised" style="left:428px;top:1849px">Raised: <b>$25,000.00</b></div>
<svg class="abs" style="left:556px;top:1812px" width="88" height="88" viewBox="0 0 88 88">
  <circle cx="44" cy="44" r="38" fill="none" stroke="rgba(255,255,255,.25)" stroke-width="6"/>
  <circle cx="44" cy="44" r="38" fill="none" stroke="#0293ce" stroke-width="6" stroke-dasharray="167 239" transform="rotate(-90 44 44)"/>
  <text x="44" y="50" text-anchor="middle" fill="#fff" font-family="Poppins,sans-serif" font-size="17" font-weight="600">70%</text>
</svg>
<div class="abs raised" style="left:660px;top:1849px">Goal: <b>$25,000.00</b></div>
<span class="abs btn" style="left:521px;top:1952px">Donate Now</span>
<span class="arrow" style="left:180px;top:1832px;transform:rotate(45deg)"></span>
<span class="arrow" style="left:1008px;top:1832px;transform:rotate(-135deg)"></span>

<!-- Latest events -->
<div class="abs sec-head" style="left:164px;top:2194px;width:426px"><h3>Latest Events</h3><span class="see-all">SEE ALL</span></div>
<div class="event" style="top:2265px"><div class="date"><b>20</b><span>AUG'18</span></div><div class="body"><h4>Which is the same as saying</h4><div class="meta">◷&nbsp; Sunday (8:00 am - 9:00 am)<br>⌖&nbsp; 18 Willow Bend Lane Maple Falls</div></div></div>
<div class="event" style="top:2397px"><div class="date"><b>16</b><span>AUG'18</span></div><div class="body"><h4>If you are going to use</h4><div class="meta">◷&nbsp; Sunday (8:00 am - 9:00 am)<br>⌖&nbsp; 18 Willow Bend Lane Maple Falls</div></div></div>
<div class="event" style="top:2524px"><div class="date"><b>27</b><span>AUG'18</span></div><div class="body"><h4>Nor again is there anyone</h4><div class="meta">◷&nbsp; Sunday (8:00 am - 9:00 am)<br>⌖&nbsp; 18 Willow Bend Lane Maple Falls</div></div></div>

<!-- Latest sermons -->
<div class="abs sec-head" style="left:685px;top:2194px;width:355px"><h3>Latest Sermons</h3><span class="see-all">SEE ALL</span></div>
<div class="acc open" style="top:2277px;height:170px">But I must explain to you how
  <div class="meta" style="font-family:'Open Sans',sans-serif;font-weight:400;margin-top:18px">Message from <u>Nathaniel</u> &nbsp;&nbsp; Aug 12, 2018</div>
  <div style="margin-top:12px"><span class="iconbox"><svg width="16" height="16" viewBox="0 0 16 16"><path d="M6 12V3l8-2v9" fill="none" stroke="#9d9d9d" stroke-width="1.4"/><circle cx="4" cy="12" r="2" fill="#9d9d9d"/><circle cx="12" cy="10" r="2" fill="#9d9d9d"/></svg></span><span class="iconbox"><svg width="16" height="16" viewBox="0 0 16 16"><rect x="1" y="4" width="14" height="9" rx="2" fill="#9d9d9d"/><path d="M7 6.5v4l3.5-2z" fill="#fff"/></svg></span><span class="iconbox"><svg width="16" height="16" viewBox="0 0 16 16"><path d="M4 1h6l3 3v11H4z" fill="none" stroke="#9d9d9d" stroke-width="1.4"/></svg></span><span class="iconbox"></span></div>
</div>
<div class="acc" style="top:2473px">Who loves or pursues</div>
<div class="acc" style="top:2533px">That pleasures have to be repudiated</div>
<div class="acc" style="top:2593px">To take a trivial example</div>

<!-- History & mission -->
<div class="abs history" style="left:164px;top:2772px;width:320px">
  <h3>Our History</h3>
  <p>Many desktop publishing packages and web page editors now use Lorem Ipsum as their default model text, and a search for 'lorem ipsum' will uncover many web sites still in their infancy. Various versions have evolved over the years.</p>
  <a class="more">Learn More</a>
  <h3 style="margin-top:32px">Mission</h3>
  <p>Many desktop publishing packages and web page editors now use Lorem Ipsum as their default model text, and a search for 'lorem ipsum' will uncover many web sites still in their infancy. Various versions have evolved over the years.</p>
  <a class="more">Learn More</a>
</div>
<div class="abs quote-box"></div>
<div class="pic" style="left:619px;top:2800px;width:152px;height:165px;background:linear-gradient(160deg,#8a6a4a,#3c2c22)" role="img" aria-label="Church nave interior"></div>
<div class="pic" style="left:771px;top:2734px;width:187px;height:231px;background:linear-gradient(160deg,#7a5a9a,#b0443c 50%,#2f5a8a)" role="img" aria-label="Stained glass window of the crucifixion"></div>
<div class="pic" style="left:958px;top:2770px;width:78px;height:195px;background:linear-gradient(160deg,#9a7450,#4a3628)" role="img" aria-label="Church altar interior"></div>
<svg class="abs" style="left:832px;top:2818px" width="64" height="64" viewBox="0 0 64 64"><circle cx="32" cy="32" r="32" fill="#0293ce"/><path d="M26 21v22l18-11z" fill="#fff"/></svg>
<div class="abs quote-mark">“</div>
<p class="abs quote-text">Many desktop publishing packages and web page editors now use Lorem Ipsum as their default model text. It uses a dictionary of over 200 Latin words, combined with.</p>
<div class="abs quote-author">DANIEL R. HAYES</div>
<svg class="abs" style="left:1005px;top:3130px" width="34" height="8" viewBox="0 0 34 8"><circle cx="4" cy="4" r="3" fill="#fff"/><circle cx="16" cy="4" r="3" fill="rgba(255,255,255,.4)"/><circle cx="28" cy="4" r="3" fill="rgba(255,255,255,.4)"/></svg>

<!-- News -->
<h2 class="abs news-title">Latest News</h2>
<article class="news-card" style="left:164px">
  <div class="pic" style="left:0;top:0;width:426px;height:220px;background:linear-gradient(135deg,#c9a36a,#6b4a2c 60%,#2e2018)" role="img" aria-label="Ornate golden cross in a church"></div>
  <div class="body"><div class="d">Aug 12, 2018</div><h4>On the other hand</h4><p>You need to be sure there isn't anything embarrassing hidden in the middle of text. All the Lorem Ipsum generators on the Internet tend to repeat predefined</p><span class="btn btn-soft">Details ›</span></div>
</article>
<article class="news-card" style="left:613px">
  <div class="pic" style="left:0;top:0;width:426px;height:220px;background:linear-gradient(135deg,#d9c7ae,#7a5a40 55%,#2a1e18)" role="img" aria-label="Open holy bible resting on a table"></div>
  <div class="body"><div class="d">Aug 12, 2018</div><h4>On the other hand</h4><p>You need to be sure there isn't anything embarrassing hidden in the middle of text. All the Lorem Ipsum generators on the Internet tend to repeat predefined</p><span class="btn btn-soft">Details ›</span></div>
</article>

<!-- Subscribe band -->
<div class="abs subscribe"></div>
<div class="abs logo" style="left:160px;top:3906px"><span class="logo-mark"></span>Gracefield<small>CHURCH THEME</small></div>
<div class="abs" style="left:475px;top:3904px;width:260px;height:40px;background:var(--dark-2);color:#8d9096;font-size:12px;line-height:40px;padding-left:18px">Email address</div>
<div class="abs" style="left:668px;top:3904px;color:#fff;font-family:Poppins,sans-serif;font-size:11px;font-weight:600;line-height:40px;letter-spacing:1px">SUBMIT ›</div>

<!-- Footer -->
<div class="abs footer" style="left:164px;top:4020px;width:280px">
  <h4>Contact Us</h4>
  <p>420 Linden Grove Road, Suite 12 Maple Falls, OR 97401</p>
  <p>E: hello@gracefield.org</p>
  <p>P: +000 555 0142 880</p>
</div>
<div class="pic" style="left:475px;top:4020px;width:250px;height:124px;background:linear-gradient(135deg,#8a6a50,#3a3a40 50%,#b08a60)" role="img" aria-label="Grid of church community photos"></div>
<svg class="abs" style="left:584px;top:4066px" width="32" height="32" viewBox="0 0 32 32"><circle cx="16" cy="16" r="16" fill="#1b1d21"/><rect x="10" y="10" width="12" height="12" rx="3" fill="none" stroke="#fff" stroke-width="1.5"/><circle cx="16" cy="16" r="3" fill="none" stroke="#fff" stroke-width="1.5"/></svg>
<div class="abs footer" style="left:777px;top:4020px;width:263px">
  <h4>Useful Links</h4>
  <div style="display:flex;gap:60px"><ul><li>FAQ</li><li>Privacy Policy</li><li>Terms &amp; Conditions</li></ul><ul><li>Account</li><li>Cart</li><li>Checkout</li></ul></div>
</div>
<div class="abs" style="left:160px;top:4238px;width:880px;border-top:1px solid var(--line)"></div>
<svg class="abs" style="left:586px;top:4250px" width="28" height="28" viewBox="0 0 28 28"><circle cx="14" cy="14" r="14" fill="#f1f1f1"/><path d="M10 16l4-4 4 4" fill="none" stroke="#111418" stroke-width="1.5"/></svg>
<footer class="abs bottom"><span>© 2018 Gracefield All Rights Reserved</span><nav><span>Home</span><span>About Us</span><span>Sermon</span><span>Events</span></nav></footer>

</body>
</html>
```